simplify or redesing image

Look Up For Your Health
Tech neck or text neck is becoming a major issue due to all mobile devices and the poor posture we have using them.
Simplify this image or design a new take on it that would convey the same message.
It would be great to have it in vector graphics.
Think more public awareness message, flyers, print-on shirts.

Target Market(s)

people with poor posture

Industry/Entity Type

healthcare

```html
<!DOCTYPE html>
<html lang="en">
<head>
<meta charset="utf-8">
<title>Look Up For Your Health</title>
<link rel="stylesheet" href="https://fonts.googleapis.com/css2?family=Montserrat:wght@300;600;800&display=swap">
<style>
  :root {
    --sky-light: #8dbcd9;
    --sky-mid: #6ea5cb;
    --sky-deep: #4f88b3;
    --spine-blue: #1f63b0;
    --spine-shade: #7fa6cc;
    --screen-grey: #c4c4c4;
    --ink-white: #ffffff;
  }
  html, body {
    margin: 0;
    padding: 0;
    width: 1200px;
    height: 2504px;
    overflow: hidden;
  }
  .poster {
    position: relative;
    width: 1200px;
    height: 2504px;
    overflow: hidden;
    background: radial-gradient(ellipse 70% 55% at 50% 55%, var(--sky-light) 0%, var(--sky-mid) 55%, var(--sky-deep) 100%);
    font-family: "Montserrat", sans-serif;
    color: var(--ink-white);
  }
  .headline {
    position: absolute;
    top: 205px;
    left: 0;
    width: 100%;
    text-align: center;
    margin: 0;
    line-height: 1;
  }
  .headline-strong {
    display: block;
    font-weight: 600;
    font-size: 208px;
    letter-spacing: 4px;
  }
  .headline-light {
    display: block;
    margin-top: 58px;
    font-weight: 300;
    font-size: 162px;
    letter-spacing: 6px;
  }
  .posture-illustration {
    position: absolute;
    inset: 0;
  }
  .spine-upright {
    position: absolute;
    left: 590px;
    top: 900px;
    width: 220px;
    height: 1120px;
    border-radius: 110px;
    background: linear-gradient(180deg, rgba(127, 166, 204, 0.85), rgba(127, 166, 204, 0.55));
    transform: rotate(-10deg);
  }
  .spine-bent {
    position: absolute;
    left: 390px;
    top: 1060px;
    width: 240px;
    height: 1140px;
    border-radius: 120px;
    background: linear-gradient(180deg, var(--spine-blue), #2a6fbb);
    transform: rotate(-17deg);
  }
  .supporting-hands {
    position: absolute;
    left: 370px;
    top: 2020px;
    width: 580px;
    height: 520px;
    border-radius: 48% 48% 0 0;
    background: radial-gradient(ellipse 60% 70% at 50% 70%, rgba(255, 255, 255, 0.95) 0%, rgba(255, 255, 255, 0.75) 60%, rgba(255, 255, 255, 0) 100%);
  }
  .phone-icon {
    position: absolute;
    left: 40px;
    top: 690px;
    width: 360px;
    height: 400px;
  }
  .health-word {
    position: absolute;
    left: 895px;
    top: 1360px;
    margin: 0;
    font-weight: 800;
    font-size: 220px;
    letter-spacing: 6px;
    line-height: 1;
    transform: translate(-50%, -50%) rotate(80deg);
    white-space: nowrap;
  }
</style>
</head>
<body>
  <main class="poster">
    <h1 class="headline">
      <span class="headline-strong">LOOK UP</span>
      <span class="headline-light">FOR YOUR</span>
    </h1>
    <div class="posture-illustration" role="img" aria-label="Illustration of a blue spine bent forward beneath a smartphone, a faded upright spine behind it, held up by two open white hands">
      <div class="spine-upright" aria-hidden="true"></div>
      <div class="spine-bent" aria-hidden="true"></div>
      <div class="supporting-hands" aria-hidden="true"></div>
    </div>
    <svg class="phone-icon" viewBox="0 0 360 400" aria-hidden="true">
      <g transform="rotate(-20 180 200)">
        <rect x="70" y="40" width="220" height="330" rx="30" fill="var(--spine-blue)"/>
        <rect x="92" y="72" width="176" height="246" rx="6" fill="var(--screen-grey)"/>
        <circle cx="180" cy="344" r="13" fill="var(--sky-light)"/>
      </g>
    </svg>
    <p class="health-word">HEALTH</p>
  </main>
</body>
</html>
```